Create a modifyable PDF

Hello,

We have a three modifiable PDF's which have been designed in Illustrator that require updating. Two documents require a complete replacement of the text while the 3rd document has minor changes.
Updates

I have attached two examples of the minor changes to 1 PDF document and a sample of the PDF where the content needs to be updated from a word document.

```html
<!DOCTYPE html>
<html lang="en">
<head>
<meta charset="utf-8">
<title>Client Benefits and Litigation Form – Page 6</title>
<link href="https://fonts.googleapis.com/css2?family=Source+Sans+3:wght@400&display=swap" rel="stylesheet">
<style>
  :root {
    --accent: #f26130;
    --label-fill: #d1d2d4;
    --rule: #5a5a5a;
    --ink: #231f20;
    --paper: #ffffff;
  }
  * { margin: 0; padding: 0; box-sizing: border-box; }
  html, body { width: 927px; height: 1200px; overflow: hidden; background: var(--paper); }
  body { font-family: "Source Sans 3", "Myriad Pro", Arial, sans-serif; color: var(--ink); font-size: 14px; }
  .page { position: relative; width: 927px; height: 1200px; }
  .band { position: absolute; left: 0; width: 927px; height: 12px; background: var(--accent); }
  .band--top { top: 0; }
  .band--bottom { bottom: 0; }

  .form-table { position: absolute; left: 77px; top: 51px; width: 774px; height: 1058px; border: 1px solid var(--rule); }
  .row { position: absolute; left: 0; width: 772px; border-bottom: 1px solid var(--rule); }
  .row:last-child { border-bottom: none; }
  .row--heading { background: var(--label-fill); }
  .row__label { position: absolute; left: 0; top: 0; bottom: 0; width: 348px; background: var(--label-fill); border-right: 1px solid var(--rule); }

  .txt { position: absolute; white-space: nowrap; line-height: 16px; letter-spacing: 0.1px; }
  .caps { text-transform: uppercase; }
  .hint { position: absolute; font-size: 9.5px; line-height: 10px; white-space: nowrap; word-spacing: 6px; }
  .blank { position: absolute; height: 0; border-bottom: 1px solid var(--ink); }
  .slash { position: absolute; line-height: 16px; }
  .box { position: absolute; width: 16px; height: 16px; border: 1px solid var(--ink); background: var(--paper); }

  .footer-code { position: absolute; left: 77px; top: 1145px; font-size: 13px; }
  .page-number { position: absolute; left: 458px; top: 1139px; font-size: 14px; }
</style>
</head>
<body>
<main class="page">
  <div class="band band--top"></div>

  <section class="form-table">
    <div class="row row--heading" style="top:0;height:38px;">
      <span class="txt caps" style="left:13px;top:13px;">7.&nbsp;&nbsp; Provide detail of any disability benefits your client is receiving through:</span>
    </div>
    <div class="row" style="top:38px;height:72px;">
      <div class="row__label">
        <span class="txt caps" style="left:37px;top:18px;">A.</span>
        <span class="txt caps" style="left:60px;top:18px;">Ontario Disability Support<br>Program or Social Assistance</span>
      </div>
    </div>
    <div class="row" style="top:110px;height:76px;">
      <div class="row__label">
        <span class="txt caps" style="left:37px;top:30px;">B.&nbsp;&nbsp; Canada Pension Plan</span>
      </div>
    </div>
    <div class="row" style="top:186px;height:140px;">
      <div class="row__label">
        <span class="txt caps" style="left:60px;top:54px;">Short or Long Term Benefits<br>Through Employment</span>
        <span class="txt caps" style="left:37px;top:54px;">C.</span>
      </div>
    </div>
    <div class="row" style="top:326px;height:120px;">
      <div class="row__label">
        <span class="txt caps" style="left:13px;top:8px;">8.&nbsp;&nbsp; Estimated Timing for Resolution</span>
      </div>
    </div>
    <div class="row row--heading" style="top:446px;height:41px;">
      <span class="txt caps" style="left:13px;top:13px;">F.&nbsp;&nbsp; If litigation is a tort claim, complete below:</span>
    </div>
    <div class="row" style="top:487px;height:73px;">
      <div class="row__label"><span class="txt caps" style="left:13px;top:12px;">1.&nbsp;&nbsp; Jurisdiction / Court</span></div>
    </div>
    <div class="row" style="top:560px;height:60px;">
      <div class="row__label"><span class="txt caps" style="left:13px;top:10px;">2.&nbsp;&nbsp; Is litigation under simplified<br><span style="padding-left:23px;">Procedures</span></span></div>
    </div>
    <div class="row" style="top:620px;height:119px;">
      <div class="row__label"><span class="txt caps" style="left:13px;top:15px;">3.&nbsp;&nbsp; Have proceedings been filed?</span></div>
    </div>
    <div class="row" style="top:739px;height:161px;">
      <div class="row__label"><span class="txt caps" style="left:13px;top:19px;">4.&nbsp;&nbsp; Discoveries</span></div>
    </div>
    <div class="row" style="top:900px;height:157px;">
      <div class="row__label"><span class="txt caps" style="left:13px;top:22px;">5.&nbsp;&nbsp; Mediation</span></div>
    </div>
  </section>

  <!-- Benefit amounts -->
  <span class="txt" style="left:446px;top:96px;">Amount (or Pre-Termination Amount):</span>
  <span class="txt" style="left:446px;top:135px;">$</span>
  <div class="blank" style="left:458px;top:149px;width:146px;"></div>
  <span class="txt" style="left:619px;top:135px;">per</span>
  <div class="blank" style="left:646px;top:149px;width:146px;"></div>

  <span class="txt" style="left:446px;top:172px;">Amount (or Pre-Termination Amount):</span>
  <span class="txt" style="left:446px;top:210px;">$</span>
  <div class="blank" style="left:458px;top:224px;width:146px;"></div>
  <span class="txt" style="left:619px;top:210px;">per</span>
  <div class="blank" style="left:646px;top:224px;width:146px;"></div>

  <span class="txt" style="left:446px;top:250px;">Amount (or Pre-Termination Amount):</span>
  <span class="txt" style="left:446px;top:289px;">$</span>
  <div class="blank" style="left:458px;top:303px;width:146px;"></div>
  <span class="txt" style="left:619px;top:289px;">per</span>
  <div class="blank" style="left:646px;top:303px;width:146px;"></div>

  <span class="txt" style="left:446px;top:333px;">Termination Date:</span>
  <div class="blank" style="left:590px;top:347px;width:61px;"></div>
  <span class="slash" style="left:653px;top:333px;">/</span>
  <div class="blank" style="left:658px;top:347px;width:61px;"></div>
  <span class="slash" style="left:721px;top:333px;">/</span>
  <div class="blank" style="left:726px;top:347px;width:66px;"></div>
  <span class="hint" style="left:616px;top:353px;">(DD &nbsp;/ &nbsp;&nbsp;&nbsp;MM &nbsp;&nbsp;&nbsp;/ &nbsp;&nbsp;YYYY)</span>

  <!-- Timing -->
  <div class="box" style="left:446px;top:390px;"></div><span class="txt" style="left:470px;top:390px;">2013</span>
  <div class="box" style="left:446px;top:415px;"></div><span class="txt" style="left:470px;top:415px;">2014</span>
  <div class="box" style="left:446px;top:441px;"></div><span class="txt" style="left:470px;top:441px;">2015</span>
  <div class="box" style="left:446px;top:466px;"></div>
  <div class="blank" style="left:469px;top:481px;width:146px;"></div>

  <!-- Simplified procedures -->
  <div class="box" style="left:446px;top:621px;"></div><span class="txt" style="left:470px;top:621px;">Yes</span>
  <div class="box" style="left:446px;top:645px;"></div><span class="txt" style="left:470px;top:645px;">No</span>

  <!-- Proceedings -->
  <span class="txt" style="left:446px;top:687px;">COURT FILE NO:</span>
  <div class="blank" style="left:553px;top:701px;width:146px;"></div>
  <div class="box" style="left:446px;top:716px;"></div><span class="txt" style="left:470px;top:716px;">Not Yet Commenced</span>
  <div class="box" style="left:446px;top:738px;"></div><span class="txt" style="left:470px;top:738px;">Closed</span>
  <div class="box" style="left:446px;top:760px;"></div><span class="txt" style="left:470px;top:760px;">Open</span>

  <!-- Discoveries -->
  <span class="txt" style="left:446px;top:810px;">Scheduled For:</span>
  <div class="blank" style="left:553px;top:825px;width:61px;"></div><span class="slash" style="left:617px;top:810px;">/</span>
  <div class="blank" style="left:621px;top:825px;width:63px;"></div><span class="slash" style="left:687px;top:810px;">/</span>
  <div class="blank" style="left:691px;top:825px;width:64px;"></div>
  <span class="hint" style="left:579px;top:831px;">(DD &nbsp;/ &nbsp;&nbsp;&nbsp;MM &nbsp;&nbsp;&nbsp;/ &nbsp;&nbsp;YYYY)</span>

  <span class="txt" style="left:446px;top:868px;">Completed:</span>
  <div class="blank" style="left:553px;top:882px;width:61px;"></div><span class="slash" style="left:617px;top:868px;">/</span>
  <div class="blank" style="left:621px;top:882px;width:63px;"></div><span class="slash" style="left:687px;top:868px;">/</span>
  <div class="blank" style="left:691px;top:882px;width:64px;"></div>
  <span class="hint" style="left:579px;top:888px;">(DD &nbsp;/ &nbsp;&nbsp;&nbsp;MM &nbsp;&nbsp;&nbsp;/ &nbsp;&nbsp;YYYY)</span>
  <div class="box" style="left:446px;top:913px;"></div><span class="txt" style="left:470px;top:913px;">HAVE NOT BEEN SCHEDULED</span>

  <!-- Mediation -->
  <span class="txt" style="left:446px;top:973px;">Scheduled For:</span>
  <div class="blank" style="left:553px;top:987px;width:61px;"></div><span class="slash" style="left:617px;top:973px;">/</span>
  <div class="blank" style="left:621px;top:987px;width:63px;"></div><span class="slash" style="left:687px;top:973px;">/</span>
  <div class="blank" style="left:691px;top:987px;width:64px;"></div>
  <span class="hint" style="left:579px;top:993px;">(DD &nbsp;/ &nbsp;&nbsp;&nbsp;MM &nbsp;&nbsp;&nbsp;/ &nbsp;&nbsp;YYYY)</span>

  <span class="txt" style="left:446px;top:1030px;">Completed:</span>
  <div class="blank" style="left:553px;top:1044px;width:61px;"></div><span class="slash" style="left:617px;top:1030px;">/</span>
  <div class="blank" style="left:621px;top:1044px;width:63px;"></div><span class="slash" style="left:687px;top:1030px;">/</span>
  <div class="blank" style="left:691px;top:1044px;width:64px;"></div>
  <span class="hint" style="left:579px;top:1050px;">(DD &nbsp;/ &nbsp;&nbsp;&nbsp;MM &nbsp;&nbsp;&nbsp;/ &nbsp;&nbsp;YYYY)</span>
  <div class="box" style="left:446px;top:1075px;"></div><span class="txt" style="left:470px;top:1075px;">HAVE NOT BEEN SCHEDULED</span>

  <span class="footer-code">{022013}</span>
  <span class="page-number">6</span>

  <div class="band band--bottom"></div>
</main>
</body>
</html>
```